Human Resource Consulting practice needs a business card design

We need a business card design (double sided colour) for our Human Resource (HR) consulting practice in regional New South Wales, australia. Our business name is Staffwise Partners. We support small and medium business across the Mid North Coast of New South Wales by providing them with outsourced HR support, services and products to help them achieve compliance with workplace legislation and across all areas of the employment lifecycle from recruitment to termination and everything in between. Our corporate colours are hot pink and black. The final design should communicate professionalism, trust, people focus.
I have attached the current (old) business card for your reference.

Target Market(s)

Business owners and high level managers

Industry/Entity Type

Business

Contact Information for Business Card

Name
Title
Phone no
Mobile no
Address
PO Box
email address
website

Colors
e34197

Requirements
Must have
• Tempate for changing business card personal details including Name, position title, mobile number, email address.
• Keep current logo and colours as per attached
• Logo must be presented in 2 colours or black only not white
Nice to have
• One side logo and graphic only other side logo and personal details
Should not have
• Should not be the same as the current version (attached) but a modern interpretation.
• Does not need a busy reverse side with our list of services as per current version. I feel this is too busy.
• No photos

```html
<!DOCTYPE html>
<html lang="en">
<head>
<meta charset="utf-8">
<title>Staffwise Partners – Business Card</title>
<link rel="stylesheet" href="https://fonts.googleapis.com/css2?family=Lato:wght@400;700&display=swap">
<style>
  :root {
    --page-bg: #d9d2c8;
    --card-bg: #f4f3f1;
    --pink: #d8337f;
    --pink-deep: #b8226a;
    --pink-light: #e34197;
    --ink: #1d1d1f;
    --band-text: rgba(255, 255, 255, 0.82);
    --icon: rgba(30, 20, 30, 0.75);
  }
  * { box-sizing: border-box; margin: 0; padding: 0; }
  html, body {
    width: 1200px;
    height: 970px;
    overflow: hidden;
    background: var(--page-bg);
    font-family: "Lato", sans-serif;
  }
  .card {
    position: absolute;
    left: 172px;
    top: 270px;
    width: 856px;
    height: 475px;
    border-radius: 22px;
    background: var(--card-bg);
    overflow: hidden;
    box-shadow: 0 10px 30px rgba(0, 0, 0, 0.18);
  }
  .brand {
    position: absolute;
    left: 40px;
    top: 90px;
  }
  .brand-name {
    font-size: 40px;
    font-weight: 700;
    color: var(--pink);
    letter-spacing: -0.5px;
  }
  .person {
    position: absolute;
    right: 66px;
    top: 86px;
    text-align: right;
  }
  .person-name {
    font-size: 31px;
    font-weight: 700;
    color: var(--pink);
    line-height: 1.2;
  }
  .person-title {
    font-size: 28px;
    font-weight: 400;
    color: var(--ink);
    line-height: 1.25;
  }
  .band {
    position: absolute;
    left: 0;
    top: 275px;
    width: 100%;
    height: 200px;
    background: linear-gradient(100deg, var(--pink-light) 0%, var(--pink) 45%, var(--pink-deep) 100%);
  }
  .contacts {
    position: absolute;
    left: 32px;
    top: 48px;
    list-style: none;
  }
  .contacts li {
    display: flex;
    align-items: center;
    gap: 12px;
    height: 29px;
    font-size: 21px;
    color: var(--band-text);
  }
  .contacts svg {
    width: 22px;
    height: 22px;
    fill: var(--icon);
  }
  .address {
    position: absolute;
    right: 271px;
    top: 78px;
    text-align: right;
    font-size: 21px;
    line-height: 29px;
    color: var(--band-text);
    font-style: normal;
  }
</style>
</head>
<body>
  <article class="card">
    <div class="brand">
      <span class="brand-name">Staffwise Partners</span>
    </div>

    <div class="person">
      <p class="person-name">Megan Hale</p>
      <p class="person-title">Principal Consultant</p>
    </div>

    <section class="band">
      <ul class="contacts">
        <li>
          <svg viewBox="0 0 24 24" aria-hidden="true"><path d="M3 8c0-2 2-4 9-4s9 2 9 4v2h-5V8H8v2H3zM6 11h12l2 9H4zm6 2a3 3 0 1 0 0 6 3 3 0 0 0 0-6z"/></svg>
          02 6500 4181
        </li>
        <li>
          <svg viewBox="0 0 24 24" aria-hidden="true"><path d="M7 2h10a2 2 0 0 1 2 2v16a2 2 0 0 1-2 2H7a2 2 0 0 1-2-2V4a2 2 0 0 1 2-2zm0 3v13h10V5zm5 14.2a1 1 0 1 0 0 1.6 1 1 0 0 0 0-1.6z"/></svg>
          0400 555 218
        </li>
        <li>
          <svg viewBox="0 0 24 24" aria-hidden="true"><path d="M2 5h20v14H2zm2 2v.5l8 6 8-6V7zm0 3v7h16v-7l-8 6z"/></svg>
          megan@staffwise.com.au
        </li>
        <li>
          <svg viewBox="0 0 24 24" aria-hidden="true"><path d="M12 2a10 10 0 1 0 0 20 10 10 0 0 0 0-20zm-1 2.1V8H7.6A8 8 0 0 1 11 4.1zm2 0A8 8 0 0 1 16.4 8H13zM5.3 10H11v4H5.3a8 8 0 0 1 0-4zm7.7 0h5.7a8 8 0 0 1 0 4H13zm-5.4 6H11v3.9A8 8 0 0 1 7.6 16zm5.4 0h3.4a8 8 0 0 1-3.4 3.9z"/></svg>
          www.staffwise.com.au
        </li>
      </ul>

      <address class="address">
        P.O. Box 318<br>
        Seaview Heads<br>
        NSW 2441
      </address>
    </section>
  </article>
</body>
</html>
```